Harborline Imaging of Michigan Brochure

We need a color brochure to highlight to our customers, patients, and referring physicians what we do, why the patients should visit our business compared to our competition. I want to emphasis that we are most concerning with delivering excellent patient care in regards to safety, an excellent patient experience and delivering high quality, meaningful imaging reports by the best radiologists.

I would like to add additional pictures to the brochure that, but not certain what to include some generic patient pictures, sports players, or family pictures that will connect with our potential clients. Any ideas are welcome.

Target Market(s)

patient and referring docs

Industry/Entity Type

Medical Imaging

Colors
0355a3
ffffff

Requirements
Must have
• a consistent look and feel with our website www.harborlineimagingofmichigan.example to have a unified "brand"
Nice to have
• clean professional look

```html
<!DOCTYPE html>
<html lang="en">
<head>
<meta charset="utf-8">
<title>Harborline Imaging of Michigan Brochure</title>
<link href="https://fonts.googleapis.com/css2?family=Source+Sans+3:wght@400;600&display=swap" rel="stylesheet">
<style>
  :root {
    --brand-blue: #0f74bd;
    --heading-blue: #0e6db5;
    --sky: #b9d8ee;
    --mist: #d8e8f5;
    --wave-mid: #8fbfe2;
    --text: #4a4a4a;
    --white: #ffffff;
    --photo-a: #e9ecef;
    --photo-b: #5f6770;
    --sign-a: #7a8a5a;
    --sign-b: #3c3c44;
  }
  * { margin: 0; padding: 0; box-sizing: border-box; }
  html, body { width: 1200px; height: 927px; overflow: hidden; background: var(--brand-blue); }
  .brochure {
    position: relative; width: 1200px; height: 927px; overflow: hidden;
    font-family: "Source Sans 3", sans-serif; color: var(--text);
  }
  .backdrop { position: absolute; inset: 0; }
  .section-title {
    position: absolute; font-weight: 400; color: var(--heading-blue);
    font-size: 35px; line-height: 1; letter-spacing: -0.2px;
  }
  .body-copy {
    position: absolute; font-size: 12.6px; line-height: 16.4px; text-align: justify;
  }
  .about-title { left: 54px; top: 150px; }
  .about-copy { left: 54px; top: 201px; width: 490px; }
  .why-title { left: 54px; top: 471px; }
  .why-col-left { left: 54px; top: 522px; width: 236px; }
  .why-col-right { left: 306px; top: 522px; width: 237px; }
  .sign-photo {
    position: absolute; left: 55px; top: 580px; width: 235px; height: 202px;
    background: linear-gradient(180deg, var(--sign-a) 0%, var(--sign-b) 60%, #b9b2a8 100%);
  }
  .team-photo {
    position: absolute; left: 599px; top: 90px; width: 601px; height: 433px;
    background: linear-gradient(110deg, var(--photo-a) 0%, #c9cfd6 35%, var(--photo-b) 75%, #2e3338 100%);
  }
  .expertise-title { left: 654px; top: 552px; }
  .expertise-copy { left: 654px; top: 602px; width: 490px; }
  .expertise-copy strong { font-weight: 600; }
  .plain { text-align: left; }
  .site-url {
    position: absolute; top: 882px; font-size: 18px; color: var(--white);
  }
  .site-url.left { left: 38px; }
  .site-url.right { right: 38px; }
</style>
</head>
<body>
<div class="brochure">
  <svg class="backdrop" width="1200" height="927" viewBox="0 0 1200 927" aria-hidden="true">
    <rect width="1200" height="927" fill="var(--brand-blue)"/>
    <path d="M0 118 C 300 60, 720 50, 1200 160 L1200 927 L0 927 Z" fill="var(--sky)"/>
    <path d="M0 145 C 300 88, 720 78, 1200 195 L1200 927 L0 927 Z" fill="var(--white)"/>
    <path d="M820 927 C 950 760, 1080 700, 1200 660 L1200 927 Z" fill="var(--mist)"/>
    <path d="M0 770 C 400 835, 850 815, 1200 715 L1200 927 L0 927 Z" fill="var(--mist)"/>
    <path d="M0 788 C 400 858, 850 845, 1200 745 L1200 927 L0 927 Z" fill="var(--wave-mid)"/>
    <path d="M0 800 C 400 870, 850 862, 1200 765 L1200 927 L0 927 Z" fill="var(--brand-blue)"/>
  </svg>

  <h2 class="section-title about-title">About Harborline Imaging</h2>
  <p class="body-copy about-copy">Harborline Imaging of Michigan, a division of Brennard and Associates, P.C., was established in 2015. We identified a need in our communities to provide a better product for our patients when choosing MRI providers. As a physician owned practice, we pride ourselves on providing High Quality, Accurate Reports, Rapid Results (a final report within 24 hours), availability for consultations/discussion with the radiologists, and Convenient care for our patients without having to get lost in the maze of a hospital.<br>Brennard and Associates, PC is a full service imaging and interventional radiology group composed of 10 Michigan based, board certified radiologists with subspecialty training in Neuroradiology, Musculoskeletal Radiology, Body Imaging, Women’s Imaging, Nuclear Radiology, and Interventional Radiology. Our group through partnering with physicians and health care institutions is committed to provide quality, timely, and efficient services with the ultimate goal of providing better health care to our patients and their physicians. Since our inception in 1979, we have had a strong history of providing high quality imaging services to Southeastern and Central Michigan. We look forward to being a complete solution for your imaging needs.</p>

  <h2 class="section-title why-title">Why Harborline Imaging?</h2>
  <p class="body-copy why-col-left">Harborline Imaging of Michigan puts patient care at the center of all we do. Whether your dealing with a knee injury or a complex</p>
  <div class="sign-photo" role="img" aria-label="Photo of the roadside building sign outside the imaging center"></div>
  <p class="body-copy why-col-right">cancer diagnosis, compassionate care is part of Harborline Imaging of Michigan. Harborline Imaging of Michigan utilizes Norvane’s equipment, with its unique short bore design and advanced acquisition technology, this allows for improved patient comfort, openness, and reduced scan times. You can be confident that our radiologists will deliver consistent, accurate, timely, and dependable reports that you and your doctor can rely on to have a meaningful impact in your care plan and treatment decisions. From diagnosis, to treatment, and recovery, our team works with your physician to quickly and accurately address your medical needs.</p>

  <div class="team-photo" role="img" aria-label="Photo of a radiologist in a white coat at a reading station with MRI scans on several monitors"></div>

  <h2 class="section-title expertise-title">Our areas of Expertise</h2>
  <p class="body-copy expertise-copy">With our diverse subspecialty trained radiologists, Harborline Imaging of Michigan will provide expertise in imaging all areas of the body. We have neuroradiologists that are trained to evaluate diseases of the brain and spine, musculoskeletal radiologist that are the experts in imaging of sports injuries and bone/muscle tumors, as well as body imaging radiologists which specialize in the imaging evaluation of abdominal and pelvis diseases. We perform MRI exams both with and without intravenous contrast and we are able to perform MRI arthrogram exams or all joints.<br><span class="plain"><strong>Insurances accepted:</strong><br>For your convenience we participate with nearly all insurance carriers.<br>We also have Self-pay options for those patients with high<br>deductibles or no insurance.</span></p>

  <div class="site-url left">www.harborlineimagingofmichigan.example</div>
  <div class="site-url right">www.harborlineimagingofmichigan.example</div>
</div>
</body>
</html>
```